IT Services company requires a services website design with integrated blog

We at Brindle Harbour Systems primarily provide application migration consultancy (e.g. moving applications from Plexor OS 4 to Plexor 9) and application virtualization (e.g. Norvane StackPod) consultancy.This process is commonly known as 'packaging' but doesnt involve cardboard boxes ;) (however, I am happy to use that visual analogy if you want to use any box graphics) We also provide application compatibility testing, software auditing and application portfolio management.

We are looking for a complete redesign of our current horrible diy attempt at a website at www.example-vendorhub.test. We have had created a rebranded logo (attached files and fonts) and a rebranded business card (also attached) We would like the website to match the same/similar colors and styling as these.

I want to redisgn the website so that the main focus of this website is to show our subject matter expertise with a blog and should take up most of the websites real estate and focus on the home screen. Then if the customer wants, they can use our services to help them in their own application migration/deployment projects by browsing our details in links/buttons somewhere
Updates

In any of the designs, please do not include my Quellbright or Norvane partnerships.  Thank you

Target Market(s)

Application packagers / engineers looking for technical articles

Application migration project managers

Industry/Entity Type

Real Estate

Requirements
Must have
• This site is primarily a blog site. The blog should have buttons to share each article on social media site. It should be easy for me to create or edit new blog articles (have technical skills but not creative ones). Each article should also allow for comments (do not require approval but should allow for admin removal) but do not add like/vote buttons because i do not expect large enough traffic and could be determental.

There should be a contact page to host contact information and an email box that goes to enquiries@example-vendorhub.test

The other pages should include About us and Services (placeholder text to be used as current site text needs overhauling but original text can be used in the design just remember when placing that the text may shorten or increase etc.)

All text has to be easily editable (no over use of text in images where possible)
Nice to have
• An email notification of new comments to articles sent to webadmin@example-vendorhub.test

Newsletter subscription
Should not have
• Do not include vote/like buttons or website counters. Initial traffic is not going to be large enough to warrant these features and may reflect badly on the site.

No logon features. Site content and commenting should be open access

No opinion polls

No why choose us section from current website

Do not include partner information in new site (Quellbright and Norvane)

DO NOT JUST REPLICATE EXISTING WEBSITE FEATURES, PLEASE REFER TO THIS BRIEF. THIS SITE NEEDS TO PRIMARILY BE A BLOG

```html
<!DOCTYPE html>
<html lang="en">
<head>
<meta charset="utf-8">
<title>Brindle Harbour Systems</title>
<link rel="stylesheet" href="https://fonts.googleapis.com/css2?family=PT+Sans:ital,wght@0,400;0,700;1,400&family=PT+Sans+Narrow:wght@400;700&display=swap">
<style>
:root{
  --blue:#4a6fd8;
  --blue-dark:#2f55c4;
  --blue-band:#1d57a8;
  --ink:#333;
  --ink-soft:#555;
  --red:#d9161c;
  --orange:#f6a800;
  --page-dark:#000;
  --footer:#141414;
}
*{margin:0;padding:0;box-sizing:border-box}
html,body{width:886px;height:1200px;overflow:hidden;background:var(--page-dark)}
body{font-family:"PT Sans",sans-serif;color:var(--ink);position:relative}
.abs{position:absolute}
.narrow{font-family:"PT Sans Narrow",sans-serif}

/* header */
.topline{left:0;top:0;width:886px;height:4px;background:var(--blue)}
.header{left:0;top:4px;width:886px;height:81px;background:linear-gradient(#fff,#f2f2f2)}
.brand{left:120px;top:28px;display:flex;align-items:center;gap:8px}
.brand-mark{width:16px;height:16px;background:var(--blue)}
.brand-name{font-size:22px;color:#555;font-weight:400}
.search{left:538px;top:33px;display:flex;box-shadow:0 3px 4px rgba(0,0,0,.15)}
.search-field{width:175px;height:17px;border:1px solid #ccc;background:#fff;font-size:8.5px;color:#999;padding:2px 5px}
.search-btn{width:46px;height:17px;background:#555;color:#fff;font-size:8.5px;text-align:center;line-height:17px}

/* nav */
.nav{left:0;top:85px;width:886px;height:44px;background:linear-gradient(#5a5a5a,#1e1e1e 55%,#111);border-bottom:1px solid #888}
.nav-item{top:0;height:43px;line-height:43px;color:#fff;font-size:13px;text-align:center}
.nav-item.is-active{background:linear-gradient(#5b80e6,var(--blue-dark))}
.nav-divider{top:6px;width:1px;height:32px;background:#666}

/* hero */
.hero-band{left:0;top:129px;width:886px;height:288px;background:linear-gradient(90deg,#113f86,var(--blue-band) 30%,#1e64bb 70%,#123f85)}
.hero-frame{left:95px;top:148px;width:709px;height:250px;background:#f4f4f4;border-radius:4px;box-shadow:0 0 6px rgba(0,0,0,.4)}
.hero-image{left:105px;top:156px;width:690px;height:234px;border-radius:3px;background:radial-gradient(ellipse at 55% 40%,#7fb9d8,#2f6f94 45%,#0b2a40 90%)}
.hero-caption{left:105px;top:243px;width:302px;height:91px;background:rgba(40,50,60,.65);color:#fff;padding:10px 15px}
.hero-caption h1{font-weight:400;font-size:17px;margin-bottom:5px}
.hero-caption p{font-size:8px;line-height:15px}
.pager{top:365px;width:14px;height:15px;font-size:9px;color:#fff;background:#111;text-align:center;line-height:15px}
.pager.is-current{background:var(--orange)}

/* main panel */
.main{left:94px;top:421px;width:479px;height:702px;background:#fff;border-radius:3px}
.section-title{font-size:16px;font-weight:700;color:#333}
.section-title span{color:var(--blue)}
.rule{height:1px;background:#e3e3e3}
.intro p{font-size:9px;line-height:15px;color:#333;width:425px}
.btn{background:var(--blue);color:#fff;font-size:8.5px;text-align:center;border-radius:3px;box-shadow:0 1px 2px rgba(0,0,0,.3)}

.article{left:107px;width:452px;height:136px;border:1px solid #ddd;border-radius:3px;background:linear-gradient(#fbfbfb,#fff);box-shadow:0 0 4px rgba(0,0,0,.08)}
.article-title{left:8px;top:9px;font-size:12.5px;font-weight:700;color:var(--blue)}
.article-meta{left:8px;top:25px;font-size:7.5px;color:#555}
.article-thumb{left:11px;top:46px;width:104px;height:76px;border:3px solid #fff;box-shadow:0 0 3px rgba(0,0,0,.35)}
.article-text{left:122px;top:51px;width:318px;font-size:7.6px;line-height:10.5px;color:#555;text-align:justify}
.share{left:122px;top:102px;display:flex;gap:6px}
.share-label{height:14px;padding:0 5px;border:1px solid #bbb;border-radius:2px;background:linear-gradient(#fff,#e6e6e6);font-size:7.5px;font-weight:700;color:#333;line-height:12px}
.article .btn{left:384px;top:100px;width:52px;height:18px;line-height:18px}

/* sidebar */
.tab{top:421px;width:109px;height:30px;line-height:30px;text-align:center;font-size:14px;border-radius:3px 3px 0 0}
.tab.is-active{left:583px;background:linear-gradient(#5b80e6,var(--blue-dark));color:#fff}
.tab.is-idle{left:695px;background:linear-gradient(#fafafa,#e3e3e3);color:#444}
.tab-panel{left:583px;top:450px;width:221px;height:281px;background:#fff;border-radius:0 0 3px 3px}
.post{left:10px;width:205px}
.post-thumb{left:0;top:0;width:76px;height:58px;border:1px solid #999}
.post-title{left:78px;top:0;font-size:9px;color:var(--red)}
.post-text{left:81px;top:14px;width:120px;font-size:7.6px;line-height:10.3px;color:#555;text-align:justify}
.post-date{left:81px;top:46px;font-size:7.5px;color:var(--red)}

.news{left:583px;top:745px;width:221px;height:230px;background:#fff;border:5px solid #c8c8c8;border-radius:4px}
.news-head{left:8px;top:7px;width:197px;height:27px;background:linear-gradient(#5b80e6,var(--blue-dark));border-radius:3px;border:2px solid #fff;box-shadow:0 0 2px rgba(0,0,0,.4);color:#fff;font-size:15px;padding-left:9px;line-height:22px}
.news-item{left:12px;width:184px}
.news-title{font-size:9px;color:var(--blue);text-transform:uppercase}
.news-date{font-size:7.8px;color:#444;margin-top:1px}
.news-text{font-size:7.8px;line-height:13px;color:#444;text-align:justify;margin-top:2px}

.newsletter{left:585px;top:990px;width:219px;height:131px;background:#fff;border-radius:4px}
.newsletter-title{left:15px;top:8px;font-size:15px;font-weight:700;color:var(--blue)}
.newsletter .rule{left:15px;top:30px;width:190px}
.newsletter-label{left:14px;top:44px;font-size:9.5px;color:#333}
.newsletter-field{left:15px;top:64px;width:181px;height:23px;border:1px solid #ccc;border-radius:2px;box-shadow:inset 0 1px 3px rgba(0,0,0,.15);font-size:8px;font-style:italic;color:#888;padding:6px 11px}
.newsletter-btn{left:115px;top:98px;width:82px;height:21px;background:var(--orange);border-radius:3px;color:#fff;font-size:10px;font-weight:700;text-align:center;line-height:21px}

/* footer */
.footer{left:0;top:1137px;width:886px;height:58px;background:var(--footer)}
.social{top:1153px;width:19px;height:19px;border-radius:2px}
.footer-links{right:88px;top:1147px;font-size:8px;color:#ddd;text-align:right;line-height:13px}
.bottomline{left:0;top:1195px;width:886px;height:5px;background:var(--blue)}
</style>
</head>
<body>

<div class="abs topline"></div>
<header class="abs header"></header>
<div class="abs brand"><span class="brand-mark"></span><span class="brand-name">Brindle Harbour Systems</span></div>
<div class="abs search"><div class="search-field">type your word here</div><div class="search-btn">SEARCH</div></div>

<nav class="abs nav narrow">
  <div class="abs nav-item is-active" style="left:122px;width:79px">HOME</div>
  <div class="abs nav-item" style="left:201px;width:77px">ABOUT US</div>
  <div class="abs nav-divider" style="left:278px"></div>
  <div class="abs nav-item" style="left:278px;width:95px">OUR SERVICES</div>
  <div class="abs nav-divider" style="left:373px"></div>
  <div class="abs nav-item" style="left:373px;width:98px">CONTACT US</div>
</nav>

<section>
  <div class="abs hero-band" role="img" aria-label="Blue circuit board background"></div>
  <div class="abs hero-frame"></div>
  <div class="abs hero-image" role="img" aria-label="Finger pressing a glowing touchscreen button among translucent tiles"></div>
  <div class="abs hero-caption">
    <h1>Welcome to Our Site</h1>
    <p>Nemo enim ipsam voluptatem quia voluptas sit aspernatur aut odit aut fugit, sed quia consequuntur magni dolores eos qui ratione voluptatem sequi nesciunt. Neque porro quisquam est.</p>
  </div>
  <div class="abs pager is-current" style="left:735px">1</div>
  <div class="abs pager" style="left:752px">2</div>
  <div class="abs pager" style="left:769px">3</div>
</section>

<main class="abs main">
  <h2 class="abs section-title narrow" style="left:23px;top:15px">Welcome <span>Brindle Harbour Systems</span></h2>
  <div class="abs rule" style="left:23px;top:39px;width:430px"></div>
  <div class="abs intro" style="left:24px;top:45px">
    <p>We have a wide range of experience in all aspects of software logistics.&nbsp; We can assist in managing your software from purchase to delivery and beyond, for small and large enterprise software migration projects, software packaging for vendors and application hosting for cloud service operators.</p>
    <p style="margin-top:14px">We offer the highest most efficient standards in application virtualization software packaging and management.</p>
    <p style="margin-top:14px">contact us today for more information</p>
  </div>
  <div class="abs btn" style="left:398px;top:154px;width:52px;height:19px;line-height:19px">More &gt;&gt;</div>
  <h2 class="abs section-title narrow" style="left:23px;top:180px;font-size:15px">Latest Articles</h2>
  <div class="abs rule" style="left:23px;top:202px;width:400px"></div>
  <div class="abs narrow" style="left:418px;top:662px;font-size:11px;font-weight:700;color:#333">View All</div>
</main>

<article class="abs article" style="top:630px">
  <h3 class="abs article-title narrow">Loreum Ipsum Dollar Sit Amet natus Voli[tatem</h3>
  <div class="abs article-meta">Built by Sed perpiciatis Saturday, June 1, 2013</div>
  <div class="abs article-thumb" style="background:linear-gradient(135deg,#6fc4ee,#1f5fa8 55%,#0c2344)" role="img" aria-label="Computer hardware in blue light"></div>
  <p class="abs article-text">Sed ut perspiciatis unde omnis iste natus error sit voluptatem accusantium.ut perspiciatis unde omnis iste natus error sit voluptatem accusantium.Sed ut perspiciatis unde omnis iste natus error sit voluptatem accusantium.ut perspiciatis unde omnis iste natus error sit voluptatem accusantium.</p>
  <div class="abs share"><span class="share-label">Post</span><span class="share-label">Share</span></div>
  <div class="abs btn">More &gt;&gt;</div>
</article>

<article class="abs article" style="top:782px">
  <h3 class="abs article-title narrow">Loreum Ipsum Dollar Sit Amet natus Voli[tatem</h3>
  <div class="abs article-meta">Built by Sed perpiciatis Saturday, June 1, 2013</div>
  <div class="abs article-thumb" style="background:linear-gradient(135deg,#8a6a52,#c7a98f 45%,#4d6f9c)" role="img" aria-label="Office worker at a desk with binders"></div>
  <p class="abs article-text">Sed ut perspiciatis unde omnis iste natus error sit voluptatem accusantium.ut perspiciatis unde omnis iste natus error sit voluptatem accusantium.Sed ut perspiciatis unde omnis iste natus error sit voluptatem accusantium.ut perspiciatis unde omnis iste natus error sit voluptatem accusantium.</p>
  <div class="abs share"><span class="share-label">Post</span><span class="share-label">Share</span></div>
  <div class="abs btn">More &gt;&gt;</div>
</article>

<article class="abs article" style="top:934px">
  <h3 class="abs article-title narrow">Loreum Ipsum Dollar Sit Amet natus Voli[tatem</h3>
  <div class="abs article-meta">Built by Sed perpiciatis Saturday, June 1, 2013</div>
  <div class="abs article-thumb" style="background:linear-gradient(180deg,#e8b048,#f1ece2 40%,#6a6a70)" role="img" aria-label="Group of people standing before an event banner"></div>
  <p class="abs article-text">Sed ut perspiciatis unde omnis iste natus error sit voluptatem accusantium.ut perspiciatis unde omnis iste natus error sit voluptatem accusantium.Sed ut perspiciatis unde omnis iste natus error sit voluptatem accusantium.ut perspiciatis unde omnis iste natus error sit voluptatem accusantium.</p>
  <div class="abs share"><span class="share-label">Post</span><span class="share-label">Share</span></div>
  <div class="abs btn">More &gt;&gt;</div>
</article>

<aside>
  <div class="abs tab is-active narrow">LATEST</div>
  <div class="abs tab is-idle narrow">POPULAR</div>
  <div class="abs tab-panel">
    <div class="abs post" style="top:19px">
      <div class="abs post-thumb" style="background:linear-gradient(135deg,#9ee2ee,#1f8aa6 50%,#0c3440)" role="img" aria-label="Hand touching a glowing button"></div>
      <div class="abs post-title">Excepteur sint occaecat.</div>
      <p class="abs post-text">Sed ut perspiciatis unde omnis iste natus error sit voluptatem accusantium.</p>
      <div class="abs post-date">May 3, 2013</div>
    </div>
    <div class="abs post" style="top:101px">
      <div class="abs post-thumb" style="background:linear-gradient(135deg,#d7ecfb,#3d87d6 50%,#103f88)" role="img" aria-label="Globe on a blue digital background"></div>
      <div class="abs post-title">Excepteur sint occaecat.</div>
      <p class="abs post-text">Sed ut perspiciatis unde omnis iste natus error sit voluptatem accusantium.</p>
      <div class="abs post-date">May 3, 2013</div>
    </div>
    <div class="abs post" style="top:183px">
      <div class="abs post-thumb" style="background:linear-gradient(180deg,#4d8fd6,#b9d8f0 55%,#6aa83a)" role="img" aria-label="Hand placing puzzle pieces against a sky and meadow"></div>
      <div class="abs post-title">Excepteur sint occaecat.</div>
      <p class="abs post-text">Sed ut perspiciatis unde omnis iste natus error sit voluptatem accusantium.</p>
      <div class="abs post-date">May 3, 2013</div>
    </div>
    <div class="abs btn" style="left:151px;top:247px;width:52px;height:18px;line-height:18px">More &gt;&gt;</div>
  </div>

  <div class="abs news">
    <div class="abs news-head narrow">Latest News</div>
    <div class="abs news-item" style="top:50px">
      <div class="news-title">New article series</div>
      <div class="news-date">Tuesday, 19 June 2012 16:47</div>
      <p class="news-text">Brindle Harbour Systems are happy to announce a new series of articles on application packaging</p>
    </div>
    <div class="abs news-item" style="top:127px">
      <div class="news-title">Services update</div>
      <div class="news-date">Tuesday, 19 June 2012 16:47</div>
      <p class="news-text">We have expanded our compatibility testing so that we can continue to offer competitive solutions in migration projects</p>
    </div>
    <div class="abs btn narrow" style="left:156px;top:192px;width:49px;height:19px;line-height:19px;font-size:10px">More</div>
  </div>

  <div class="abs newsletter">
    <div class="abs newsletter-title narrow">Newsletter</div>
    <div class="abs rule"></div>
    <div class="abs newsletter-label">Sign up for Newsletter</div>
    <div class="abs newsletter-field">Your Email Id</div>
    <div class="abs newsletter-btn narrow">Subscribe</div>
  </div>
</aside>

<footer class="abs footer"></footer>
<div class="abs social" style="left:95px;background:#3b5b98" aria-label="Social link"></div>
<div class="abs social" style="left:124px;background:#3aa8e0" aria-label="Social link"></div>
<div class="abs social" style="left:152px;background:#3a3a3a" aria-label="Social link"></div>
<div class="abs social" style="left:181px;background:#f08c1c" aria-label="Feed link"></div>
<div class="abs social" style="left:209px;background:#cc1a1a" aria-label="Video link"></div>
<div class="abs social" style="left:238px;background:#6f8ea6" aria-label="Email link"></div>
<div class="abs footer-links">Privacy &nbsp;|&nbsp; FAQ &nbsp;|&nbsp; Contact &nbsp;|&nbsp; Terms &amp; Conditions<br>© 2013 example-vendorhub.test, All Rights Reserved</div>
<div class="abs bottomline"></div>

</body>
</html>
```